Skin care manufacturer looking for packaging design for new skin care brand.

We need a design and logo for a skin care brand to be sold at retail stores and online in the United States and Europe. The design will be for 1.7oz - 2oz serums that will not have a retail box. The name of the brand is Velora Fen and should be a luxurious brand that is approachable. The brand will consist of 4 face serums - Vitamin C, Collagen, Retinol and Hyaluronic Acid that all contain Dead Sea Minerals. Images shown are for inspiration only. Color of bottles can be varied based on design and bottles can be screen printed or labeled.

```html
<!DOCTYPE html>
<html lang="en">
<head>
<meta charset="UTF-8">
<title>Velora Fen Face Serum Label</title>
<link href="https://fonts.googleapis.com/css2?family=Arimo:wght@400&display=swap" rel="stylesheet">
<style>
  :root {
    --page: #ecedef;
    --navy: #0e2168;
    --gold: #8f6e1f;
    --gold-soft: rgba(143, 110, 31, 0.15);
    --white: #ffffff;
    --badge-text: #1d2f7a;
  }
  html, body {
    margin: 0;
    padding: 0;
    width: 810px;
    height: 1200px;
    overflow: hidden;
    background: var(--page);
    font-family: "Arimo", Arial, sans-serif;
  }
  .canvas {
    position: relative;
    width: 810px;
    height: 1200px;
  }
  .label {
    position: absolute;
    left: 40px;
    top: 442px;
    width: 730px;
    height: 316px;
    background: var(--navy);
    overflow: hidden;
  }
  .label-frame {
    position: absolute;
    left: 16px;
    top: 16px;
    right: 16px;
    bottom: 16px;
    border: 4px solid var(--gold);
  }
  .brand-name {
    position: absolute;
    top: 36px;
    left: 0;
    width: 100%;
    text-align: center;
    color: var(--gold);
    font-size: 27px;
    line-height: 1;
  }
  .brand-tagline {
    position: absolute;
    top: 67px;
    left: 0;
    width: 100%;
    text-align: center;
    color: var(--gold);
    font-size: 14px;
    letter-spacing: 4px;
    line-height: 1;
  }
  .actives {
    position: absolute;
    top: 111px;
    left: 0;
    width: 100%;
    text-align: center;
    color: var(--white);
    font-size: 20px;
    line-height: 25px;
  }
  .wave-small {
    position: absolute;
    left: 251px;
    top: 156px;
    width: 72px;
    height: 36px;
    border-radius: 36px 36px 0 0;
    background: radial-gradient(ellipse at 50% 100%, var(--gold) 55%, var(--gold-soft) 100%);
  }
  .wave-large {
    position: absolute;
    left: 309px;
    top: 169px;
    width: 212px;
    height: 125px;
    border-radius: 110px 60px 0 0;
    background: radial-gradient(ellipse at 55% 100%, var(--gold) 50%, var(--gold-soft) 100%);
  }
  .feature-badge {
    position: absolute;
    left: 248px;
    top: 186px;
    width: 125px;
    height: 63px;
    box-sizing: border-box;
    padding: 9px 0 0 13px;
    background: var(--gold);
    border-radius: 4px 32px 32px 4px;
    color: var(--badge-text);
    font-size: 17px;
    line-height: 22px;
  }
  .net-volume {
    position: absolute;
    left: 257px;
    top: 271px;
    color: var(--white);
    font-size: 13px;
  }
</style>
</head>
<body>
<div class="canvas">
  <div class="label">
    <div class="label-frame"></div>
    <div class="brand-name">Velora Fen</div>
    <div class="brand-tagline">face serum</div>
    <div class="actives">Hyaluronic Acid<br>Retinol</div>
    <div class="wave-small" role="img" aria-label="Gold stylised ocean wave crest ornament"></div>
    <div class="wave-large" role="img" aria-label="Large gold stylised ocean wave ornament"></div>
    <div class="feature-badge">Vitamin C<br>+ Collagen</div>
    <div class="net-volume">1.7 oz</div>
  </div>
</div>
</body>
</html>
```